Large multi-office optometry business opening a Dry Eye Spa and needs sign.

Business name/sign info: Brenwick Dry Eye Institute, (555) 362-4817
Backlit pole sign at office entrance on a very busy street
Sign dimensions: 53" tall x 136.5" wide
State of the art Dry Eye Spa for treatment of all forms of dry eye and ocular surface disease. Also, have aesthetics treatments (IPL, Low Level Light Treatment, etc.)

Target Market(s)

People who are suffering from: dryness, burning, foreign body sensation, itching, fluctuating vision, tired eyes, etc.

Industry/Entity Type

Optometry and aesthetics

Colors
0054AA
0677BA
7BADD7
CADEEF
E8F1F8

Requirements
Must have
• Business name, phone number, subliminal message of relief in a glance or short look.
Nice to have
• Cool, relief, soothing sense.
Should not have
• Too much information or too busy.

```html
<!DOCTYPE html>
<html lang="en">
<head>
<meta charset="utf-8">
<title>Brenwick Dry Eye Institute – Sign</title>
<link rel="stylesheet" href="https://fonts.googleapis.com/css2?family=Montserrat:wght@800&family=Poppins:wght@300&family=Roboto:wght@700&display=swap">
<style>
  :root{
    --navy:#0054AA;
    --blue:#0677BA;
    --sky:#7BADD7;
    --mist:#CADEEF;
    --ice:#E8F1F8;
    --cream:#FEFDF6;
    --red:#DE2620;
    --ink:#1616C4;
    --green:#1DB98A;
    --green-pale:#CDEBDD;
  }
  html,body{margin:0;padding:0;overflow:hidden;background:#fff;}
  .sign{
    position:relative;width:1200px;height:468px;overflow:hidden;
    background:linear-gradient(135deg,#1B8FD6 0%,var(--blue) 45%,var(--navy) 100%);
  }
  .panel{
    position:absolute;left:14px;top:14px;width:1172px;height:440px;
    background:var(--cream);border-radius:10px;overflow:hidden;
  }
  .wave-texture{
    position:absolute;left:0;top:0;width:145px;height:140px;
    background:radial-gradient(ellipse at 40% 40%,var(--green-pale),rgba(205,235,221,0) 70%);
  }
  .pill{
    position:absolute;left:172px;top:-20px;width:116px;height:110px;
    background:linear-gradient(180deg,#5E9FE0,var(--sky));
    border-radius:0 0 58px 58px;
  }
  .green-blob{
    position:absolute;left:0;top:268px;width:190px;height:190px;
    background:linear-gradient(160deg,#1FA878,#14C59D);
    border-radius:0 80px 0 0;
  }
  .droplets{
    position:absolute;left:38px;top:128px;width:300px;height:300px;
    background:radial-gradient(ellipse at 55% 60%,#FFFFFF 0%,var(--ice) 40%,var(--mist) 75%,rgba(202,222,239,0) 100%);
    border-radius:50% 50% 46% 46%;
  }
  .tab{position:absolute;left:482px;top:0;width:440px;height:70px;}
  .tab-label{
    position:absolute;left:482px;top:0;width:440px;height:70px;
    display:flex;align-items:center;justify-content:center;
    font:800 45px/1 "Montserrat",sans-serif;color:#fff;letter-spacing:0.5px;
  }
  .business-name{
    position:absolute;left:300px;top:95px;width:800px;margin:0;text-align:center;
    font:800 70px/80px "Montserrat",sans-serif;color:var(--red);letter-spacing:1px;
  }
  .symptoms{
    position:absolute;left:300px;top:252px;width:800px;margin:0;text-align:center;
    font:300 22px/31px "Poppins",sans-serif;color:var(--ink);
  }
  .phone{
    position:absolute;left:470px;top:334px;width:469px;height:87px;
    border-radius:10px;
    background:linear-gradient(90deg,var(--navy) 0%,#0A6CC2 50%,#1790D4 100%);
    display:flex;align-items:center;justify-content:center;
    font:700 50px/1 "Roboto",sans-serif;color:#fff;letter-spacing:1px;
  }
</style>
</head>
<body>
<div class="sign">
  <div class="panel">
    <div class="wave-texture" role="img" aria-label="Flowing green line texture"></div>
    <div class="pill"></div>
    <div class="green-blob"></div>
    <div class="droplets" role="img" aria-label="Two glossy water droplets"></div>
  </div>

  <svg class="tab" viewBox="0 0 440 70" aria-hidden="true">
    <defs>
      <linearGradient id="tabFill" x1="0" y1="0" x2="1" y2="0">
        <stop offset="0" stop-color="#0A6CC2"/>
        <stop offset="1" stop-color="#0054AA"/>
      </linearGradient>
    </defs>
    <path d="M0 0 H440 C418 0 412 70 388 70 H52 C28 70 22 0 0 0 Z" fill="url(#tabFill)"/>
  </svg>
  <div class="tab-label">OPENING NOW</div>

  <h1 class="business-name">BRENWICK<br>DRY EYE INSTITUTE</h1>
  <p class="symptoms">Dryness - Burning - Foreign Body Sensation - Itching<br>Fluctuating Vision - Tired Eyes</p>
  <div class="phone">(555) 362-4817</div>
</div>
</body>
</html>
```